Open Red Harbor.. a non profit that seeks to stomp out skin cancer .. quiet paths toward opening red

Simple letterhead incorporating logo

Industry/Entity Type

Non Profit

Font styles to use
Sans Serif

Colors

Designer to choose colors to be used in the design.

```html
<!DOCTYPE html>
<html lang="en">
<head>
<meta charset="utf-8">
<title>Open Red Harbor — Letterhead</title>
<link rel="stylesheet" href="https://fonts.googleapis.com/css2?family=Archivo:wght@700;800&display=swap">
<style>
  :root {
    --navy: #252a3a;
    --yellow: #f5e000;
    --paper: #ffffff;
    --label-blue: #2e6a9e;
    --ink: #111111;
    --backdrop: #e9e6e1;
  }
  * { margin: 0; padding: 0; box-sizing: border-box; }
  html, body { width: 1200px; height: 1000px; overflow: hidden; }
  body {
    background: var(--backdrop);
    position: relative;
    font-family: "Archivo", Arial, sans-serif;
  }
  .sheet {
    position: absolute;
    top: 47px;
    height: 893px;
    background: var(--paper);
    overflow: hidden;
    box-shadow: 0 2px 10px rgba(0,0,0,0.15);
  }
  .sheet--curves { left: 7px; width: 587px; }
  .sheet--sidebar { left: 604px; width: 589px; }
  .sheet svg.decor { position: absolute; left: 0; top: 0; }
  .brand {
    position: absolute;
    width: 112px; height: 112px;
    border-radius: 50%;
    background: var(--navy);
    display: flex; align-items: center; justify-content: center;
    text-align: center;
    color: var(--yellow);
    font-weight: 700;
    font-size: 17px;
    line-height: 1.1;
    padding: 14px;
  }
  .sheet--curves .brand { left: 239px; top: 4px; }
  .sheet--sidebar .brand { left: 296px; top: 12px; }
  .sample-title {
    position: absolute;
    top: 400px;
    color: var(--navy);
    font-weight: 800;
    font-size: 58px;
    letter-spacing: 1px;
  }
  .sheet--curves .sample-title { left: 44px; }
  .sheet--sidebar .sample-title { left: 262px; }
  .contact-row {
    position: absolute;
    top: 770px; left: 0; width: 587px;
  }
  .contact-item {
    position: absolute;
    display: flex; flex-direction: column; align-items: center;
    color: var(--label-blue);
    font-weight: 700;
    font-size: 15px;
  }
  .contact-item svg { margin-bottom: 6px; }
  .sidebar {
    position: absolute;
    left: 0; top: 103px; width: 177px; height: 790px;
    background: var(--navy);
    border-top: 26px solid var(--yellow);
  }
  .sidebar-tab {
    position: absolute;
    left: 10px; width: 175px; height: 29px;
    display: flex; align-items: center; gap: 6px;
    padding-left: 8px;
    color: var(--ink);
    font-weight: 800;
    font-size: 14px;
    letter-spacing: 2px;
    background: var(--yellow);
    clip-path: polygon(6px 0, 100% 0, 100% 100%, 6px 100%, 0 50%);
  }
</style>
</head>
<body>

  <section class="sheet sheet--curves">
    <svg class="decor" width="587" height="893" viewBox="0 0 587 893" aria-hidden="true">
      <path d="M0 75 Q293 160 587 81 L587 196 Q293 100 0 201 Z" fill="var(--yellow)"/>
      <path d="M45 893 Q300 820 560 893 Z" fill="var(--yellow)"/>
    </svg>
    <div class="brand">Open Red Harbor</div>
    <h1 class="sample-title">SAMPLE 1</h1>

    <div class="contact-row">
      <div class="contact-item" style="left:24px;">
        <svg width="20" height="30" viewBox="0 0 20 30"><path d="M12 2 L16 4 L13 11 L10 10 Q7 17 11 23 L14 21 L17 26 L12 29 Q3 22 5 12 Q7 5 12 2Z" fill="var(--navy)"/></svg>
        PHONE
      </div>
      <div class="contact-item" style="left:165px;">
        <svg width="30" height="28" viewBox="0 0 30 28" fill="none" stroke="var(--navy)" stroke-width="2"><rect x="8" y="3" width="14" height="9"/><rect x="2" y="12" width="26" height="10"/><line x1="6" y1="17" x2="24" y2="17"/></svg>
        FAX
      </div>
      <div class="contact-item" style="left:313px;">
        <svg width="36" height="26" viewBox="0 0 36 26" fill="none" stroke="var(--navy)" stroke-width="2"><rect x="2" y="3" width="32" height="20"/><path d="M2 3 L18 15 L34 3 M2 23 L14 12 M34 23 L22 12"/></svg>
        EMAIL
      </div>
      <div class="contact-item" style="left:476px;">
        <svg width="32" height="30" viewBox="0 0 32 30"><circle cx="16" cy="15" r="13" fill="var(--paper)" stroke="var(--navy)" stroke-width="2"/><path d="M6 9 Q12 6 15 10 Q13 15 9 14 Q6 16 5 13Z M17 16 Q22 14 25 18 Q23 25 19 26 Q17 21 17 16Z M19 5 Q24 6 26 10 Q22 10 19 5Z" fill="var(--navy)"/></svg>
        WEBSITE
      </div>
    </div>
  </section>

  <section class="sheet sheet--sidebar">
    <div class="brand">Open Red Harbor</div>
    <div class="sidebar"></div>

    <div class="sidebar-tab" style="top:231px;">
      <svg width="16" height="22" viewBox="0 0 20 30"><path d="M12 2 L16 4 L13 11 L10 10 Q7 17 11 23 L14 21 L17 26 L12 29 Q3 22 5 12 Q7 5 12 2Z" fill="var(--ink)"/></svg>
      PHONE
    </div>
    <div class="sidebar-tab" style="top:355px;">
      <svg width="30" height="22" viewBox="0 0 30 28" fill="none" stroke="var(--ink)" stroke-width="2"><rect x="8" y="3" width="14" height="9"/><rect x="2" y="12" width="26" height="10"/><line x1="6" y1="17" x2="24" y2="17"/></svg>
      FAX
    </div>
    <div class="sidebar-tab" style="top:493px;">
      <svg width="32" height="22" viewBox="0 0 36 26" fill="none" stroke="var(--ink)" stroke-width="2"><rect x="2" y="3" width="32" height="20"/><path d="M2 3 L18 15 L34 3 M2 23 L14 12 M34 23 L22 12"/></svg>
      E-MAIL
    </div>
    <div class="sidebar-tab" style="top:623px;">
      <svg width="24" height="24" viewBox="0 0 32 30"><circle cx="16" cy="15" r="13" fill="var(--ink)"/><path d="M6 9 Q12 6 15 10 Q13 15 9 14 Q6 16 5 13Z M17 16 Q22 14 25 18 Q23 25 19 26 Q17 21 17 16Z" fill="var(--yellow)"/></svg>
      WEBSITE
    </div>

    <h1 class="sample-title">SAMPLE 2</h1>
  </section>

</body>
</html>
```